Copper Gate Labradoodle web design

We're a new labradoodle breeder in Charleston, SC in need of a web design.

Our name is Copper Gate Labradoodles.

Site we like: http://www.fernhilldoodlery.example/
http://www.quailbrookpups.example/

Logo Font:
The ''Copper Gate'' font is called TestarossaNF and is available freely at http://www.typequarry.example/testarossa-nf.font.  The ''Labradoodles'' font is called Worstveld Sling Extra and is available freely at http://www.glyphbarn.example/WorstveldSlingExtra.php.

Requirements
Must have
• Our logo
1. Home page
2. Labradoodle F.A.Q.
3. Our doodles
4. Availability
5. Adoption Process
6. Contact us
Link/badge icon for Health Guarantee
Nice to have
• Color and font to match the logo.

An area to add pictures
Should not have
• Rainbows
Rainbow colors

```html
<!DOCTYPE html>
<html lang="en">
<head>
<meta charset="utf-8">
<title>Copper Gate Labradoodle News</title>
<link rel="stylesheet" href="https://fonts.googleapis.com/css2?family=Cinzel:wght@400;600;700&family=Source+Sans+3:ital,wght@0,400;0,600;1,600&display=swap">
<style>
  :root {
    --pink: #ee7f99;
    --pink-light: #f6a3b6;
    --pink-deep: #d9587a;
    --band-pink: #e9708f;
    --beige: #e9ddd0;
    --beige-band: #e3d4c4;
    --brown: #3a2414;
    --text-grey: #8a8480;
    --placeholder: #e4e4e4;
    --field: #ffffff;
    --white: #ffffff;
  }
  * { box-sizing: border-box; margin: 0; padding: 0; }
  html, body { width: 833px; height: 1200px; overflow: hidden; }
  body {
    position: relative;
    background: var(--white);
    font-family: "Source Sans 3", Arial, sans-serif;
    color: var(--brown);
  }

  /* Header */
  .top-bar {
    position: absolute; left: 0; top: 0; width: 833px; height: 28px;
    background: linear-gradient(#f49ab0, var(--band-pink));
  }
  .main-nav { position: absolute; top: 7px; left: 0; width: 833px; }
  .main-nav a {
    position: absolute; color: var(--white); text-decoration: none;
    font-family: "Cinzel", Georgia, serif; font-size: 12px; font-weight: 600;
    letter-spacing: 0.3px; white-space: nowrap;
  }
  .header-band {
    position: absolute; left: 0; top: 28px; width: 833px; height: 30px;
    background: var(--beige-band);
  }
  .brand-seal {
    position: absolute; border-radius: 50%;
    background: radial-gradient(circle at 50% 45%, #f59ab0, var(--pink-deep));
    box-shadow: 0 3px 6px rgba(0,0,0,0.35);
    display: flex; align-items: center; justify-content: center; text-align: center;
    font-family: "Cinzel", Georgia, serif; font-weight: 700; color: var(--white);
    line-height: 1.15;
  }
  .brand-seal--header { left: 62px; top: 6px; width: 134px; height: 134px; font-size: 13px; padding: 18px; }
  .brand-seal--footer { left: 133px; top: 842px; width: 110px; height: 106px; font-size: 11px; padding: 14px; z-index: 2; }

  /* Page heading */
  .page-title {
    position: absolute; top: 174px; width: 833px; text-align: center;
    font-family: "Cinzel", Georgia, serif; font-weight: 400; font-size: 31px;
    color: var(--brown); letter-spacing: 0.5px;
  }
  .page-subtitle {
    position: absolute; top: 220px; left: 0; width: 820px; text-align: center;
    font-size: 26px; font-weight: 400; color: var(--pink);
  }

  /* News grid */
  .news-item { position: absolute; width: 350px; height: 110px; }
  .news-thumb {
    position: absolute; left: 0; top: 0; width: 106px; height: 106px;
    background: var(--placeholder);
  }
  .news-thumb--tan { background: linear-gradient(135deg, #c98a55, #7a4a28); }
  .news-thumb--cream { background: linear-gradient(135deg, #f3f1ec, #bdb7ae); }
  .news-title {
    position: absolute; left: 121px; top: 0; white-space: nowrap;
    font-family: "Cinzel", Georgia, serif; font-weight: 600; font-size: 13.5px;
    color: var(--brown); letter-spacing: 0.6px;
  }
  .news-excerpt {
    position: absolute; left: 120px; top: 33px; width: 240px; white-space: nowrap;
    font-size: 10.6px; line-height: 13px; color: var(--text-grey);
  }
  .news-date {
    position: absolute; left: 148px; top: 80px; width: 67px; height: 18px;
    background: var(--pink); color: var(--white); border-radius: 2px;
    font-size: 10px; text-align: center; line-height: 18px;
  }
  .news-date::after {
    content: ""; position: absolute; right: 4px; bottom: -6px;
    border-left: 7px solid var(--pink); border-bottom: 6px solid transparent;
  }
  .news-more {
    position: absolute; left: 262px; top: 85px; white-space: nowrap;
    font-size: 10px; font-style: italic; font-weight: 600; color: var(--pink);
  }
  .scroll-track {
    position: absolute; left: 793px; top: 355px; width: 6px; height: 325px;
    border-radius: 3px; background: #8c8c8c;
  }

  /* Footer */
  .footer-rule { position: absolute; left: 0; top: 882px; width: 833px; height: 1px; background: #999; }
  .footer-band { position: absolute; left: 0; top: 883px; width: 833px; height: 34px; background: var(--band-pink); }
  .footer-body { position: absolute; left: 0; top: 917px; width: 833px; height: 263px; background: var(--beige); }
  .footer-nav a {
    position: absolute; left: 58px; color: var(--brown); text-decoration: none;
    font-family: "Cinzel", Georgia, serif; font-size: 15.5px; letter-spacing: 0.6px;
  }
  .social-button {
    position: absolute; left: 58px; top: 1120px; width: 174px; height: 30px;
    background: linear-gradient(#f6a9bb, var(--pink-deep)); border-radius: 2px;
    color: var(--white); font-size: 14px; font-weight: 600; text-align: center; line-height: 30px;
    box-shadow: 0 1px 2px rgba(0,0,0,0.25);
  }
  .contact-heading {
    position: absolute; left: 304px; top: 941px; font-weight: 400;
    font-family: "Cinzel", Georgia, serif; font-size: 15.5px; color: var(--brown); letter-spacing: 0.6px;
  }
  .field {
    position: absolute; left: 304px; width: 239px; background: var(--field);
    font-size: 10.5px; color: var(--brown); padding: 4px 8px;
  }
  .field--name { top: 964px; height: 22px; }
  .field--email { top: 1001px; height: 22px; }
  .field--message { top: 1033px; height: 82px; }
  .submit-button {
    position: absolute; left: 484px; top: 1126px; width: 59px; height: 25px;
    background: linear-gradient(#f6a9bb, var(--pink)); border-radius: 3px;
    color: var(--white); font-size: 10.5px; text-align: center; line-height: 25px;
  }
  .guarantee-badge { position: absolute; left: 622px; top: 963px; width: 153px; height: 153px; }
  .copyright-bar {
    position: absolute; left: 0; top: 1180px; width: 833px; height: 20px;
    background: var(--pink-light); text-align: center; line-height: 22px;
    font-family: "Cinzel", Georgia, serif; font-size: 8.5px; color: #b33a5c;
  }
</style>
</head>
<body>
  <header>
    <div class="top-bar"></div>
    <nav class="main-nav">
      <a style="left:285px">Home</a>
      <a style="left:350px">Availability</a>
      <a style="left:450px">Adoption</a>
      <a style="left:537px">Our Doodles</a>
      <a style="left:651px">Contact</a>
      <a style="left:733px">F.A.Q.</a>
    </nav>
    <div class="header-band"></div>
    <div class="brand-seal brand-seal--header">Copper Gate Labradoodles</div>
  </header>

  <main>
    <h1 class="page-title">Copper Gate Labradoodle News</h1>
    <p class="page-subtitle">Stay connected with us</p>

    <article class="news-item" style="left:53px; top:307px">
      <div class="news-thumb news-thumb--tan" role="img" aria-label="Photo of an apricot labradoodle puppy resting"></div>
      <h2 class="news-title">Events in your area</h2>
      <p class="news-excerpt">Proin gravida nibh vel velit auctor aliquet. Aenean<br>sollicitudin, lorem quis bibendum auctor, nisi elit<br>consequat ipsum, nec sagittis sem nibh id elit.</p>
      <span class="news-date">June 15</span>
      <span class="news-more">Continue reading...</span>
    </article>
    <article class="news-item" style="left:423px; top:307px">
      <div class="news-thumb news-thumb--cream" role="img" aria-label="Photo of a white labradoodle sitting"></div>
      <h2 class="news-title">Our New Facility</h2>
      <p class="news-excerpt">Proin gravida nibh vel velit auctor aliquet. Aenean<br>sollicitudin, lorem quis bibendum auctor, nisi elit<br>consequat ipsum, nec sagittis sem nibh id elit.</p>
      <span class="news-date">June 14</span>
      <span class="news-more">Continue reading...</span>
    </article>

    <article class="news-item" style="left:53px; top:467px">
      <div class="news-thumb" role="img" aria-label="Photo placeholder"></div>
      <h2 class="news-title">Local Dog News</h2>
      <p class="news-excerpt">Proin gravida nibh vel velit auctor aliquet. Aenean<br>sollicitudin, lorem quis bibendum auctor, nisi elit<br>consequat ipsum, nec sagittis sem nibh id elit.</p>
      <span class="news-date">June 13</span>
      <span class="news-more">Continue reading...</span>
    </article>
    <article class="news-item" style="left:423px; top:467px">
      <div class="news-thumb" role="img" aria-label="Photo placeholder"></div>
      <h2 class="news-title">Our New Website Is Up</h2>
      <p class="news-excerpt">Proin gravida nibh vel velit auctor aliquet. Aenean<br>sollicitudin, lorem quis bibendum auctor, nisi elit<br>consequat ipsum, nec sagittis sem nibh id elit.</p>
      <span class="news-date">June 12</span>
      <span class="news-more">Continue reading...</span>
    </article>

    <article class="news-item" style="left:53px; top:626px">
      <div class="news-thumb" role="img" aria-label="Photo placeholder"></div>
      <h2 class="news-title">Tips On Housetraining</h2>
      <p class="news-excerpt">Proin gravida nibh vel velit auctor aliquet. Aenean<br>sollicitudin, lorem quis bibendum auctor, nisi elit<br>consequat ipsum, nec sagittis sem nibh id elit.</p>
      <span class="news-date">June 11</span>
      <span class="news-more">Continue reading...</span>
    </article>
    <article class="news-item" style="left:423px; top:626px">
      <div class="news-thumb" role="img" aria-label="Photo placeholder"></div>
      <h2 class="news-title">Listening To Your Doodle</h2>
      <p class="news-excerpt">Proin gravida nibh vel velit auctor aliquet. Aenean<br>sollicitudin, lorem quis bibendum auctor, nisi elit<br>consequat ipsum, nec sagittis sem nibh id elit.</p>
      <span class="news-date">June 10</span>
      <span class="news-more">Continue reading...</span>
    </article>

    <div class="scroll-track"></div>
  </main>

  <footer>
    <div class="footer-rule"></div>
    <div class="footer-band"></div>
    <div class="footer-body"></div>
    <div class="brand-seal brand-seal--footer">Copper Gate Labradoodles</div>

    <nav class="footer-nav">
      <a style="top:941px">HOME</a>
      <a style="top:968px">AVAILABILITY</a>
      <a style="top:996px">ADOPTION</a>
      <a style="top:1023px">OUR DOODLES</a>
      <a style="top:1050px">CONTACT US</a>
      <a style="top:1078px">FAQ</a>
    </nav>
    <div class="social-button">Follow Us On Pawbook</div>

    <h3 class="contact-heading">CONTACT US</h3>
    <div class="field field--name">Name</div>
    <div class="field field--email">Email</div>
    <div class="field field--message"></div>
    <div class="submit-button">Submit</div>

    <svg class="guarantee-badge" viewBox="0 0 153 153" role="img" aria-label="Health guarantee badge">
      <defs>
        <radialGradient id="badgeFill" cx="45%" cy="40%" r="65%">
          <stop offset="0" stop-color="#f2f2f2"/>
          <stop offset="1" stop-color="#9c9c9c"/>
        </radialGradient>
      </defs>
      <circle cx="76.5" cy="76.5" r="74" fill="url(#badgeFill)"/>
    </svg>

    <div class="copyright-bar">Copyright©2013 Copper Gate Labradoodles All Rights Reserved.</div>
  </footer>
</body>
</html>
```